Financial Services Consultant needs a business card

We need a business card for a new consulting company based in Melbourne called
"Korvane Metrics". Tagline is Measure, Monitor, Save
We would like to see business card designs that are in line with the minimal style of the website www.korvane-metrics-example.com
The font I have used on the website is Proxima Nova and would like the same or similar font used on the business card with a minimal design in line with the website Two sided with "KORVANE METRICS" MEASURE, MONITOR, SAVE on one side and name, title and contact details on the otther
Updates

Hi All, thanks for your submissions, much appreciated.

I have recently added some colour to my webiste, it is hex #3a7b74 for those that wish to use it
Thanks

Hi all

thanks very much for your design submissions I am very impressed and they are much appreciated.

Interms of general feedback please find below;

Colour: I am trying to stick to a minimal design and colour scheme for my website which is still under construction, up to 3 colours( www.korvane-metrics-example.com) it is currently black and white with a small amount of blue/green but I am open to suggestion/interpretations for a consulting company.

Card: I dont mind if it has rounded edges or straight, I was thinking about using a letterpress card if possible

Detail: the detail on the card will include; Name, Title, Mobile, Personal Email, Business Email,Web,Business Address

Once again thanks for submissions

Industry/Entity Type

Business

```html
<!DOCTYPE html>
<html lang="en">
<head>
<meta charset="utf-8">
<title>Korvane Metrics – Business Card</title>
<link rel="stylesheet" href="https://fonts.googleapis.com/css2?family=Montserrat:wght@400;500&display=swap">
<style>
  :root {
    --backdrop: #463e3f;
    --card-white: #ffffff;
    --brand-teal: #2d8c8d;
    --ink: #1e1e1e;
    --on-teal: #ffffff;
  }
  * { box-sizing: border-box; margin: 0; padding: 0; }
  html, body {
    width: 1200px;
    height: 900px;
    overflow: hidden;
  }
  body {
    background: var(--backdrop);
    font-family: "Montserrat", Arial, sans-serif;
    position: relative;
  }
  .card {
    position: absolute;
    width: 560px;
    height: 320px;
    border-radius: 18px;
    overflow: hidden;
  }
  .card--front {
    left: 60px;
    top: 110px;
    background: var(--card-white);
  }
  .card--back {
    left: 580px;
    top: 470px;
    background: var(--brand-teal);
    color: var(--on-teal);
    text-align: center;
  }
  .front__name {
    position: absolute;
    top: 98px;
    width: 100%;
    text-align: center;
    font-size: 44px;
    font-weight: 500;
    letter-spacing: 1px;
    color: var(--ink);
  }
  .front__rule {
    position: absolute;
    left: 0;
    top: 200px;
    width: 100%;
    height: 2px;
    display: block;
  }
  .front__tagline {
    position: absolute;
    top: 250px;
    width: 100%;
    text-align: center;
    font-size: 17px;
    font-weight: 400;
    letter-spacing: 1.6px;
    color: var(--brand-teal);
  }
  .back__name {
    margin-top: 52px;
    font-size: 36px;
    font-weight: 500;
    letter-spacing: 1px;
  }
  .back__tagline {
    margin-top: 2px;
    font-size: 11px;
    letter-spacing: 1.4px;
  }
  .back__contact {
    list-style: none;
    margin-top: 64px;
    font-size: 17px;
    line-height: 1.3;
    letter-spacing: 0.8px;
  }
</style>
</head>
<body>
  <section class="card card--front" aria-label="Card front">
    <h1 class="front__name">KORVANE METRICS</h1>
    <svg class="front__rule" viewBox="0 0 560 2" preserveAspectRatio="none" aria-hidden="true">
      <line x1="0" y1="1" x2="560" y2="1" stroke="var(--brand-teal)" stroke-width="2"/>
    </svg>
    <p class="front__tagline">MEASURE, MONITOR, SAVE</p>
  </section>

  <section class="card card--back" aria-label="Card back">
    <h2 class="back__name">KORVANE METRICS</h2>
    <p class="back__tagline">MEASURE, MONITOR, SAVE</p>
    <ul class="back__contact">
      <li>+00 000000</li>
      <li>xxxx@mailbox-example.com</li>
      <li>xxx@korvane-metrics-example.com</li>
      <li>www.korvane-metrics-example.com</li>
      <li>Business Address</li>
    </ul>
  </section>
</body>
</html>
```